3 JPG Website Page Mockups need tidying / made into layered PSDs

Our website is aimed at creating a financial eduction site for females.

We have mockups of each page which are provided in jpeg.... but they need to be tidied up, layered into PSD (with descriptive layer names to allow coding from and no flattening - each object needs it's own layer) and we welcome any creative improvements suggested (although we are pretty happy with the way it's laid out at the moment as it is), without changing the feel, colour scheme or functionality of the site.

Three pages are needed:
Home page when not logged in
Home page when logged in
Topic header page

Please just upload the homepage to bid for the job... the winning designer will then have 5 days after they've been chosen to supply the psds of the other 2 pages .

I have also uploaded an image that can be used as a placeholder in the top box.
Thanks
Updates

As requested... Current font is Gill Sans MT

Thanks

Hi
Thanks for your designs.... For those of you still using the 4 circles (which I quite like), but haven't yet done so, could you see if you can move them around slightly to that the words don't get covered by the next circle?

Thanks

Reason: Designe has asked for An extension to work on new icons... would like to give them the time to see what they come up with, thanks

Industry/Entity Type

Financial

Requirements
Must have
• Maintain current feel & colour scheme of the website

```html
<!DOCTYPE html>
<html lang="en">
<head>
<meta charset="utf-8">
<title>The Money Muse – Home</title>
<link href="https://fonts.googleapis.com/css2?family=Cabin:wght@400;500;600;700&display=swap" rel="stylesheet">
<style>
:root{
  --teal:#0f9aa0;
  --teal-dark:#0b7f85;
  --teal-text:#4f8a9a;
  --heading:#5a8e9c;
  --sage:#a9c29c;
  --sage-dark:#6f9a63;
  --cream:#f1ecd0;
  --orange:#ff7a10;
  --orange-dark:#f05a00;
  --grey-bg:#efefef;
  --border:#2f9a97;
  --ink:#222;
  --muted:#666;
  --white:#fff;
}
*{box-sizing:border-box;margin:0;padding:0}
html,body{width:1200px;height:949px;overflow:hidden;background:var(--white);font-family:"Cabin",sans-serif;color:var(--ink)}
.page{position:relative;width:1200px;height:949px}

/* top navigation */
.topnav{position:absolute;left:0;top:0;width:1200px;height:35px;background:linear-gradient(#14aab0,var(--teal-dark))}
.topnav a{position:absolute;top:5px;color:var(--white);font-size:20px;font-weight:600;font-variant:small-caps;text-decoration:none;letter-spacing:.2px}
.home-tab{position:absolute;left:87px;top:5px;width:55px;height:30px;background:var(--grey-bg);border-radius:3px 3px 0 0}
.home-tab svg{position:absolute;left:21px;top:9px}
.locale{position:absolute;left:1051px;top:9px;color:var(--white);font-size:12px;display:flex;align-items:center;gap:5px}
.flag{width:24px;height:16px;background:#1c3f8c;border:1px solid #fff}

/* header */
.header{position:absolute;left:0;top:35px;width:1200px;height:133px;background:var(--grey-bg)}
.logo{position:absolute;left:85px;top:32px;font-size:56px;font-weight:400;letter-spacing:1px;color:#000}
.search-label{position:absolute;left:337px;top:17px;color:var(--teal-dark);font-size:17px;font-weight:600}
.search{position:absolute;left:319px;top:45px;width:443px;height:37px;background:var(--white);border:1px solid #ccc;border-radius:19px}
.search span{position:absolute;left:17px;top:8px;color:#999;font-size:17px}
.search i{position:absolute;right:10px;top:9px;width:19px;height:19px;border-radius:50%;background:var(--teal)}
.sublinks a{position:absolute;top:95px;color:var(--teal-dark);font-size:14px;text-decoration:none;text-align:center}
.sublinks a::after{content:"";display:block;margin:3px auto 0;width:8px;height:8px;border-right:2px solid var(--teal);border-bottom:2px solid var(--teal);transform:rotate(45deg)}
.pill{position:absolute;top:45px;height:37px;background:#f6f6f6;border:1px solid #ccc;border-radius:19px;font-size:14px;display:flex;align-items:center;gap:8px;padding-left:8px;color:#222}
.pill i{width:21px;height:21px;border-radius:50%;background:var(--teal-dark);display:inline-block;position:relative}
.pill i::after{content:"";position:absolute;left:6px;top:7px;width:5px;height:5px;border-right:2px solid #fff;border-top:2px solid #fff;transform:rotate(45deg)}

/* welcome row */
.welcome{position:absolute;left:105px;top:188px;font-size:24px;color:var(--heading)}
.member{position:absolute;right:88px;top:193px;font-size:15px;display:flex;align-items:center;gap:8px}
.member b{display:flex;align-items:center;gap:6px;margin-left:10px}
.member b i{width:20px;height:20px;border-radius:50%;background:var(--orange);display:inline-block}

/* hero */
.hero{position:absolute;left:87px;top:239px;width:1025px;height:264px;border:1px solid var(--border);border-radius:3px;background:linear-gradient(#f5f5f5,#dedede);overflow:hidden}
.hero h1{position:absolute;left:31px;top:18px;font-size:30px;font-weight:400;line-height:43px;color:var(--heading)}
.join{position:absolute;left:25px;top:180px;width:401px;height:64px;border-radius:32px;background:linear-gradient(#ff9a3c,var(--orange-dark));color:var(--white);font-size:31px;font-weight:700;display:flex;align-items:center;gap:22px;padding-left:20px}
.join i{width:40px;height:40px;border-radius:50%;background:var(--white);position:relative}
.join i::after{content:"";position:absolute;left:11px;top:13px;width:11px;height:11px;border-right:4px solid var(--orange);border-top:4px solid var(--orange);transform:rotate(45deg)}
.hero-photo{position:absolute;left:573px;top:0;width:452px;height:264px;background:linear-gradient(90deg,rgba(230,230,230,0) 0%,#b9b5a8 18%,#8f8a7c 55%,#6c6c6c 100%)}
.caption{position:absolute;left:888px;top:172px;width:130px;height:45px;background:rgba(255,255,255,.92);border-radius:4px;padding:6px 10px;font-size:14px;line-height:14px}
.caption small{font-size:12px;color:#444}
.pager{position:absolute;left:831px;top:225px;width:193px;height:31px;background:rgba(240,240,240,.9);border-radius:4px;font-size:12px;color:var(--teal-dark);display:flex;align-items:center;gap:14px;padding-left:10px}
.pager u{color:#222}

/* topic */
.topic{position:absolute;left:87px;top:526px;width:1025px;height:278px;border:1px solid var(--border);border-radius:3px;background:linear-gradient(#f6f6f6,#e4e4e4)}
.video{position:absolute;left:17px;top:16px;width:301px;height:245px;background:#2a2522}
.video-frame{position:absolute;left:0;top:0;width:301px;height:226px;background:linear-gradient(120deg,#5a2a22,#3a2b2a 50%,#6a5e52)}
.play{position:absolute;left:123px;top:86px;width:55px;height:55px;background:rgba(0,0,0,.8)}
.nameplate{position:absolute;left:0;top:164px;width:180px;height:46px;background:rgba(111,154,99,.9);color:#fff;padding:5px 0 0 30px;font-size:12px;letter-spacing:1.5px;line-height:11px}
.nameplate small{font-size:9px;letter-spacing:.5px}
.controls{position:absolute;left:0;top:226px;width:301px;height:19px;background:#eee;font-size:9px;color:#555;display:flex;align-items:center;gap:10px;padding-left:6px}
.controls .bar{flex:0 0 150px;height:3px;background:#aaa}
.topic-kicker{position:absolute;left:366px;top:12px;font-size:27px;color:#222}
.topic h2{position:absolute;left:366px;top:46px;font-size:34px;font-weight:400;color:var(--heading);line-height:42px}
.learn{position:absolute;left:366px;top:142px;font-size:15px;font-weight:700;color:var(--sage-dark)}
.circle{position:absolute;border-radius:50%;display:flex;flex-direction:column;align-items:center;justify-content:center;text-align:center}
.c-guide{left:472px;top:170px;width:96px;height:96px;background:#fff;border:6px solid #c7d9bd;font-size:13px;line-height:15px}
.c-guide b{font-size:19px}
.c-guide span{color:var(--sage-dark);font-size:12px}
.c-poll{left:568px;top:116px;width:150px;height:150px;background:#fff;padding:8px}
.c-poll .inner{width:134px;height:134px;border-radius:50%;background:#dce6f1;border:2px solid var(--sage);display:flex;flex-direction:column;align-items:center;justify-content:center;font-size:15px;font-weight:700}
.c-poll span{color:var(--sage-dark);font-size:12px;font-weight:400}
.c-stories{left:720px;top:94px;width:120px;height:120px;background:#fff;border:8px solid var(--cream);font-size:12px;font-weight:700;line-height:14px}
.c-stories span{color:var(--sage-dark);font-weight:400}
.c-ask{left:843px;top:97px;width:172px;height:172px;background:var(--sage);border:3px solid #c4d6ba;color:#fff;font-size:14px;line-height:17px;padding:0 16px}
.c-ask span{margin-top:10px;font-weight:600}

/* section tabs */
.tabs{position:absolute;left:87px;top:818px;width:1025px;height:131px}
.tab{position:absolute;top:0;width:128px;height:122px;text-align:center}
.tab.active{background:linear-gradient(#ff8a26,#ffb06a 85%,#fff);border-radius:3px 3px 0 0}
.tab .icon{position:absolute;left:34px;top:12px;width:60px;height:58px;border-radius:10px}
.tab span{position:absolute;left:0;top:80px;width:128px;font-size:15px;font-weight:700;color:var(--teal-text)}
.tab.active span{color:#111}
</style>
</head>
<body>
<div class="page">

  <nav class="topnav">
    <div class="home-tab"><svg width="12" height="11" viewBox="0 0 12 11"><path d="M6 0L12 5H10V11H2V5H0Z" fill="#0f9aa0"/></svg></div>
    <a style="left:160px">Polls</a>
    <a style="left:256px">Events</a>
    <a style="left:360px">Learning Centre</a>
    <a style="left:538px">Find an Adviser</a>
    <a style="left:694px">Ask a Question</a>
    <a style="left:858px">About Us</a>
    <div class="locale"><span class="flag"></span>AU ▾</div>
  </nav>

  <header class="header">
    <div class="logo">LOGO</div>
    <div class="search-label">What are you looking for?</div>
    <div class="search"><span>Search The Money Muse for....</span><i></i></div>
    <div class="sublinks">
      <a style="left:329px">Popular Searches</a>
      <a style="left:459px">Explore the Learning Centre</a>
      <a style="left:656px">Ask a Question</a>
    </div>
    <div class="pill" style="left:838px;width:145px"><i></i>Find an Adviser</div>
    <div class="pill" style="left:987px;width:125px"><i></i>Contact Us</div>
  </header>

  <div class="welcome">Welcome to the new Money Muse Site</div>
  <div class="member">Already a member? <b><i></i>Login</b><b><i></i>Forgot Password</b></div>

  <section class="hero">
    <h1>We’re building Australia’s biggest<br>community dedicated to the<br>Financial Empowerment of Women.</h1>
    <div class="join"><i></i>Join Now for FREE</div>
    <div class="hero-photo" role="img" aria-label="Two women chatting over coffee at a living room table"></div>
    <div class="caption">Helen<br><small>Member since 2006</small></div>
    <div class="pager">Previous <span>1</span><span>2</span><span>3</span><u>4</u><span>Next</span></div>
  </section>

  <section class="topic">
    <div class="video">
      <div class="video-frame" role="img" aria-label="Video still of a business founder speaking in an office"></div>
      <div class="play"><svg width="55" height="55" viewBox="0 0 55 55"><path d="M21 17L38 27.5L21 38Z" fill="#fff"/></svg></div>
      <div class="nameplate">DANA WHITFIELD<br><small>FOUNDER, CHAIR &amp; CEO<br>LEDGER &amp; LANE</small></div>
      <div class="controls">▶ ■ <span>00:00</span><span class="bar"></span><span>00:00</span></div>
    </div>
    <div class="topic-kicker">July Topic: Preparing for Retirement</div>
    <h2>Tomorrow Can Belong to Those Who<br>Prepare Today</h2>
    <div class="learn">Learn More »</div>

    <div class="circle c-guide">5 Minute<b>Guide</b><span>PDF »</span></div>
    <div class="circle c-poll"><div class="inner">
      <svg width="100" height="40" viewBox="0 0 100 40">
        <g fill="#8fb07f"><rect x="0" y="34" width="7" height="6"/><rect x="10" y="32" width="7" height="8"/><rect x="20" y="28" width="7" height="12"/><rect x="30" y="22" width="7" height="18"/><rect x="40" y="16" width="7" height="24"/><rect x="50" y="12" width="7" height="28"/><rect x="60" y="8" width="7" height="32"/><rect x="70" y="4" width="7" height="36"/><rect x="80" y="2" width="7" height="38"/><rect x="90" y="4" width="7" height="36"/></g>
      </svg>
      <div style="margin-top:8px">Take Our Poll</div><span>Vote »</span></div></div>
    <div class="circle c-stories">Real Women<br>Real Stories<span>See Videos »</span></div>
    <div class="circle c-ask">Have questions about Life Stars &amp; Planning? Ask a question or see what others have asked...<span>More »</span></div>
  </section>

  <nav class="tabs">
    <div class="tab active" style="left:0"><div class="icon" role="img" aria-label="Welcome icon of a woman" style="background:#8a5a2a"></div><span>Welcome</span></div>
    <div class="tab" style="left:133px"><div class="icon" role="img" aria-label="Calendar icon" style="background:#d8d8d8;border-top:12px solid #d43a2a"></div><span>Events</span></div>
    <div class="tab" style="left:257px"><div class="icon" role="img" aria-label="Film reel icon" style="background:#9aa0a6;border-radius:50%"></div><span>Webcasts</span></div>
    <div class="tab" style="left:379px"><div class="icon" role="img" aria-label="House icon" style="background:linear-gradient(#d9302a 45%,#e6dfcf 45%)"></div><span>My Family</span></div>
    <div class="tab" style="left:499px"><div class="icon" role="img" aria-label="Rising bar chart icon" style="background:linear-gradient(90deg,#3a9ad9,#f2c12e,#5bb84a)"></div><span>My Investments</span></div>
    <div class="tab" style="left:649px"><div class="icon" role="img" aria-label="Calendar and clock icon" style="background:#7fb3e0"></div><span>My Retirement</span></div>
    <div class="tab" style="left:775px"><div class="icon" role="img" aria-label="Handshake icon" style="background:#e0a070"></div><span>My Estate</span></div>
    <div class="tab" style="left:889px"><div class="icon" role="img" aria-label="Yoga figure icon" style="background:#f2b81c;border-radius:50%"></div><span>My Lifestyle</span></div>
  </nav>

</div>
</body>
</html>
```